Business Card Design

Copperfield Lantern Works, Inc. (CLW), located in Memphis, TN began operating on 2003. We are a certified
minority woman-owned business that genuinely takes a vested interest in our customers. We serve utilities,
government, contractors and end user markets in electrical, water, gas and industrial supplies. Our core
competency as a distributor of electrical materials has positioned us to serve business of all size. As your supply
chain partner, we arm you with the resources you need to make your supply chain more efficient. Our team
works with your team on a daily basis to help you solve problems and achieve goals. This team approach has
helped CLW customers to succeed and we can do the same for you.

NAICS Codes:
423610 Electrical Apparatus and Equipment, Wiring Supplies, and Related Equipment Merchant
Wholesalers
423510 Metal Service Centers and Other Metal Merchant Wholesalers
423720 Plumbing and Heating Equipment and Supplies (Hydronics) Merchant Wholesalers

Certifications
MBE (KRVPQAL, State of Tennessee Up-RFX and HJW), WBE (QOZRT),
WOSB, DOT (TDOT, MDOT, ALDOT, SCDOT, NCDOT, and VDOT), LOSB,
SBE, and LSB Certified
Some of Our Products Include:
. Boxes & Covers
. Conduit & Raceway
. Fittings
. Fuses
. Lamp & Ballasts
. Lighting Controls & Timers
. Lighting Fixtures
. Personal Safety
. Pipes
. Power Distribution
. Terminations Ground & Splices
. Tools & Testers
. Wire, Cords & Cable
. Wiring Devices
. Valves

Industry/Entity Type

Business

Contact Information for Business Card

Harriet M. Pendlow - President/CEO
4817 Galvin Ave., Memphis, TN 38127
901-482-6317 office, 901-482-6319 fax, 901-358-2074 cell
hmpendlow@clwgroupx.com - www.clwworksx.com

```html
<!DOCTYPE html>
<html lang="en">
<head>
<meta charset="utf-8">
<title>Copperfield Lantern Works – Business Card</title>
<link href="https://fonts.googleapis.com/css2?family=Cormorant+Garamond:wght@600;700&family=Open+Sans:wght@400;600&display=swap" rel="stylesheet">
<style>
  :root {
    --backdrop: #e9e6e1;
    --card: #ffffff;
    --charcoal: #3b3b3b;
    --charcoal-edge: #5a5a5a;
    --olive: #a7b43a;
    --olive-text: #9aa62c;
    --ink: #1e1e1e;
    --on-dark: #ffffff;
  }
  * { margin: 0; padding: 0; box-sizing: border-box; }
  html, body { width: 1200px; height: 892px; overflow: hidden; }
  body {
    background: var(--backdrop);
    font-family: "Open Sans", sans-serif;
    color: var(--ink);
    position: relative;
  }
  .card {
    position: absolute;
    left: 250px;
    width: 700px;
    height: 400px;
    background: var(--card);
    box-shadow: 0 6px 18px rgba(0,0,0,.18);
    overflow: hidden;
  }
  .card--front { top: 30px; }
  .card--back { top: 462px; }

  /* Front */
  .front-art { position: absolute; inset: 0; }
  .brand {
    position: absolute;
    left: 40px; top: 44px;
    font-family: "Cormorant Garamond", serif;
    font-weight: 700;
    font-size: 30px;
    line-height: 1.05;
    letter-spacing: 1px;
    text-transform: uppercase;
    color: var(--ink);
    display: flex;
    align-items: center;
    gap: 14px;
  }
  .brand__mark {
    width: 16px; height: 16px;
    background: var(--olive);
    border-radius: 50%;
    flex: none;
  }
  .person {
    position: absolute;
    right: 36px; top: 118px;
    text-align: right;
  }
  .person__name {
    font-family: "Cormorant Garamond", serif;
    font-weight: 700;
    font-size: 34px;
    color: var(--ink);
  }
  .person__title {
    font-size: 17px;
    color: var(--ink);
    margin-top: 2px;
  }
  .contact {
    position: absolute;
    right: 26px; top: 272px;
    list-style: none;
  }
  .contact__item {
    display: flex;
    justify-content: flex-end;
    align-items: center;
    gap: 12px;
    height: 21px;
    font-size: 15px;
    color: var(--on-dark);
  }
  .contact__icon {
    width: 16px; height: 16px;
    background: var(--on-dark);
    border-radius: 2px;
    display: flex; align-items: center; justify-content: center;
    flex: none;
  }
  .contact__icon svg { width: 12px; height: 12px; }

  /* Back */
  .products__heading {
    position: absolute;
    left: 0; right: 0; top: 34px;
    text-align: center;
    font-size: 30px;
    font-weight: 400;
    color: var(--olive-text);
  }
  .products__list {
    position: absolute;
    top: 96px;
    list-style: none;
  }
  .products__list--left { left: 70px; }
  .products__list--right { left: 400px; }
  .products__item {
    display: flex;
    align-items: center;
    gap: 14px;
    font-size: 21px;
    line-height: 31px;
  }
  .products__bullet {
    width: 10px; height: 10px;
    background: var(--ink);
    border-radius: 1px;
    flex: none;
  }
</style>
</head>
<body>

<section class="card card--front" aria-label="Business card front">
  <svg class="front-art" viewBox="0 0 700 400" preserveAspectRatio="none" aria-hidden="true">
    <path d="M0,128 C150,118 300,158 430,203 C540,238 620,250 700,250" fill="none" stroke="var(--olive)" stroke-width="11"/>
    <path d="M0,140 C150,130 300,170 430,215 C540,250 620,262 700,262 L700,400 L0,400 Z" fill="var(--charcoal)"/>
    <path d="M0,140 C150,130 300,170 430,215 C540,250 620,262 700,262" fill="none" stroke="var(--charcoal-edge)" stroke-width="3"/>
  </svg>

  <div class="brand">
    <span class="brand__mark"></span>
    <span>Copperfield<br>Lantern Works</span>
  </div>

  <div class="person">
    <div class="person__name">Harriet M. Pendlow</div>
    <div class="person__title">President/CEO</div>
  </div>

  <ul class="contact">
    <li class="contact__item">901-358-2074
      <span class="contact__icon"><svg viewBox="0 0 12 12"><rect x="3" y="1" width="6" height="10" rx="1" fill="none" stroke="#333" stroke-width="1.3"/></svg></span></li>
    <li class="contact__item">901-482-6317
      <span class="contact__icon"><svg viewBox="0 0 12 12"><path d="M2 1.5 L4.5 1.5 L5 4 L3.8 5 C4.5 6.6 5.4 7.5 7 8.2 L8 7 L10.5 7.5 L10.5 10 C5.5 10 2 6.5 2 1.5 Z" fill="#333"/></svg></span></li>
    <li class="contact__item">901-482-6319
      <span class="contact__icon"><svg viewBox="0 0 12 12"><rect x="1.5" y="4" width="9" height="6" fill="#333"/><rect x="3.5" y="1.5" width="5" height="3" fill="none" stroke="#333"/></svg></span></li>
    <li class="contact__item">hmpendlow@clwgroupx.com
      <span class="contact__icon"><svg viewBox="0 0 12 12"><rect x="1" y="2.5" width="10" height="7" fill="none" stroke="#333" stroke-width="1.2"/><path d="M1 2.5 L6 7 L11 2.5" fill="none" stroke="#333" stroke-width="1.2"/></svg></span></li>
    <li class="contact__item">www.clwworksx.com
      <span class="contact__icon"><svg viewBox="0 0 12 12"><circle cx="6" cy="6" r="4.6" fill="none" stroke="#333" stroke-width="1.2"/><path d="M1.4 6 H10.6 M6 1.4 C4 4 4 8 6 10.6 M6 1.4 C8 4 8 8 6 10.6" fill="none" stroke="#333"/></svg></span></li>
    <li class="contact__item">4817 Galvin Ave, Memphis, TN 38127
      <span class="contact__icon"><svg viewBox="0 0 12 12"><path d="M6 11 C3 7 2.5 5.8 2.5 4.5 A3.5 3.5 0 0 1 9.5 4.5 C9.5 5.8 9 7 6 11 Z" fill="#333"/><circle cx="6" cy="4.5" r="1.2" fill="#fff"/></svg></span></li>
  </ul>
</section>

<section class="card card--back" aria-label="Business card back">
  <h2 class="products__heading">Our Products</h2>
  <ul class="products__list products__list--left">
    <li class="products__item"><span class="products__bullet"></span>Boxes &amp; Covers</li>
    <li class="products__item"><span class="products__bullet"></span>Conduit &amp; Raceway</li>
    <li class="products__item"><span class="products__bullet"></span>Fittings</li>
    <li class="products__item"><span class="products__bullet"></span>Fuses</li>
    <li class="products__item"><span class="products__bullet"></span>Lamp &amp; Ballasts</li>
    <li class="products__item"><span class="products__bullet"></span>Lighting Controls &amp; Timers</li>
    <li class="products__item"><span class="products__bullet"></span>Lighting Fixtures</li>
    <li class="products__item"><span class="products__bullet"></span>Personal Safety</li>
    <li class="products__item"><span class="products__bullet"></span>Pipes</li>
  </ul>
  <ul class="products__list products__list--right">
    <li class="products__item"><span class="products__bullet"></span>Power Distribution</li>
    <li class="products__item"><span class="products__bullet"></span>Terminations Ground &amp; Splices</li>
    <li class="products__item"><span class="products__bullet"></span>Tools &amp; Testers</li>
    <li class="products__item"><span class="products__bullet"></span>Wire, Cords &amp; Cable</li>
    <li class="products__item"><span class="products__bullet"></span>Wiring Devices</li>
    <li class="products__item"><span class="products__bullet"></span>Valves</li>
  </ul>
</section>

</body>
</html>
```